Pell Nutrition Therapy needs a business card design

I need a business card design for my private practice. Green is my favorite color. I would like the back of the card to include an area for future appointment dates and time. I provide nutrition therapy to individuals, groups and families. I work a lot with adolescents and women who have eating disorders, but also work with athletes.

Reason: I received several new designs and would like to take some time reviewing them.

Target Market(s)

I am working primarily with women, but also men (mostly athletes). I work with a lot of runners. I work with people who are 14-60's.

Industry/Entity Type

Nutrition

Font styles to use
Serif
Sans Serif

Colors
9bcb3c
acd037

Requirements
Nice to have
• I would love to have 'Pell' incorporated into the design since it is my last name. If possible, I'd love to have an actual moon if it looks professional.

A picture of food could also be on the card if it is simple, but not sure how it would look with Pell. I am open to ideas for both Pell and a picture of a food item.

Other font style are fine as long as they are easy to read.

```html
<!DOCTYPE html>
<html lang="en">
<head>
<meta charset="utf-8">
<title>Pell Nutrition Therapy – Business Card</title>
<link href="https://fonts.googleapis.com/css2?family=Cabin:wght@700&family=Roboto+Condensed:wght@700&display=swap" rel="stylesheet">
<style>
  :root {
    --page: #ffffff;
    --card: #ffffff;
    --green: #9bcb3c;
    --ink: #6f6f6f;
    --line: #e4e4e4;
  }
  * { margin: 0; padding: 0; box-sizing: border-box; }
  html, body { width: 926px; height: 1200px; overflow: hidden; background: var(--page); }
  .canvas { position: relative; width: 926px; height: 1200px; }
  .card {
    position: absolute; left: 216px; width: 512px;
    background: var(--card);
    box-shadow: 0 0 10px rgba(0,0,0,0.12);
  }
  .card--front { top: 225px; height: 340px; }
  .card--back  { top: 647px; height: 343px; }

  .wordmark {
    position: absolute; display: flex; align-items: center; gap: 14px;
    font-family: "Cabin", sans-serif; font-weight: 700; color: var(--green);
    line-height: 1.15;
  }
  .wordmark__dot { flex: none; border-radius: 50%; background: var(--green); }
  .wordmark__name { text-align: center; }
  .card--front .wordmark { left: 100px; top: 108px; font-size: 31px; }
  .card--front .wordmark__dot { width: 62px; height: 62px; }
  .card--back .wordmark { left: 44px; top: 66px; font-size: 27px; }
  .card--back .wordmark__dot { width: 52px; height: 52px; }

  .stripes { position: absolute; left: 0; right: 0; top: 273px; }
  .stripes span { display: block; height: 6px; background: var(--green); margin-bottom: 7px; }

  .contact-band {
    position: absolute; left: 0; right: 0; top: 214px; height: 75px;
    background: var(--green);
    font-family: "Roboto Condensed", sans-serif; font-weight: 700; color: var(--ink);
  }
  .holder { position: absolute; left: 66px; top: 4px; font-size: 19px; }
  .address { position: absolute; left: 66px; top: 28px; font-size: 12.5px; line-height: 15px; }
  .phones { position: absolute; left: 340px; top: 30px; font-size: 14px; }
  .phones li { list-style: none; display: flex; align-items: center; gap: 10px; height: 23px; }
  .icon { flex: none; display: block; }
  .icon--mail { position: absolute; left: 32px; top: 30px; }

  .web-row {
    position: absolute; left: 0; right: 0; top: 298px; height: 26px;
    font-family: "Roboto Condensed", sans-serif; font-weight: 700; color: var(--ink); font-size: 13px;
  }
  .web-row .item { position: absolute; top: 0; display: flex; align-items: center; gap: 12px; height: 26px; }
  .web-row .item--site { left: 32px; }
  .web-row .item--email { left: 340px; }
</style>
</head>
<body>
<div class="canvas">

  <section class="card card--front">
    <div class="wordmark">
      <span class="wordmark__dot"></span>
      <span class="wordmark__name">Pell Nutrition<br>Therapy</span>
    </div>
    <div class="stripes"><span></span><span></span><span></span><span></span><span></span></div>
  </section>

  <section class="card card--back">
    <div class="wordmark">
      <span class="wordmark__dot"></span>
      <span class="wordmark__name">Pell Nutrition<br>Therapy</span>
    </div>

    <div class="contact-band">
      <p class="holder">Dana Whitfield Pell, MS, RD, LDN</p>
      <svg class="icon icon--mail" width="22" height="14" viewBox="0 0 22 14">
        <rect x="1" y="1" width="20" height="12" fill="#d8ec9e" stroke="#fff" stroke-width="1"/>
        <path d="M1 1 L11 8 L21 1" fill="none" stroke="#fff" stroke-width="1.2"/>
      </svg>
      <p class="address">Postal Address<br>4410 Maple Bend Road<br>Lakeside, TN 37000</p>
      <ul class="phones">
        <li>
          <svg class="icon" width="20" height="20" viewBox="0 0 20 20">
            <circle cx="10" cy="10" r="9" fill="#c7e283" stroke="#fff" stroke-width="1.5"/>
            <path d="M7 5 L9 7 L8 8.5 Q9.5 11 11.5 12 L13 11 L15 13 L13.5 15 Q9 14.5 5.5 9 Q5 6.5 7 5 Z" fill="#fff"/>
          </svg>
          <span>555.014.2290</span>
        </li>
        <li>
          <svg class="icon" width="20" height="20" viewBox="0 0 20 20">
            <circle cx="10" cy="10" r="9" fill="#c7e283" stroke="#fff" stroke-width="1.5"/>
            <rect x="5" y="8" width="10" height="6" rx="1" fill="#fff"/>
            <path d="M4.5 8 Q10 3.5 15.5 8" fill="none" stroke="#fff" stroke-width="1.6"/>
          </svg>
          <span>555.014.7731</span>
        </li>
      </ul>
    </div>

    <div class="web-row">
      <div class="item item--site">
        <svg class="icon" width="20" height="20" viewBox="0 0 20 20">
          <circle cx="10" cy="10" r="8.5" fill="#c7e283" stroke="var(--green)" stroke-width="1.5"/>
          <ellipse cx="10" cy="10" rx="3.5" ry="8" fill="none" stroke="#fff" stroke-width="1"/>
          <line x1="2" y1="10" x2="18" y2="10" stroke="#fff" stroke-width="1"/>
        </svg>
        <span>www.youwebsite.com</span>
      </div>
      <div class="item item--email">
        <svg class="icon" width="20" height="20" viewBox="0 0 20 20">
          <rect x="1.5" y="1.5" width="17" height="17" rx="3" fill="#c7e283" stroke="var(--green)" stroke-width="1.5"/>
          <text x="10" y="14.5" text-anchor="middle" font-family="Arial, sans-serif" font-size="12" font-weight="700" fill="#fff">@</text>
        </svg>
        <span>dpell@examplemail.net</span>
      </div>
    </div>
  </section>

</div>
</body>
</html>
```